Brisk. Technology Logistics Software platform.

A modern looking and feeling website for a logistics software platform.
We connect retailers or wholesale parcel distributors to worldwide delivery solutions.
Methods tend to be road and air transport to final mile courier companies and post offices all over the world.
Our platform is for ecommerce distribution. A customer uses BRISK to enable them to connect to worldwide companies who will track and trace the delivery of their goods.

Target Market(s)

Onllne retailers. Markert Places such as Tolvaro and Quendix. Wholesale third party logistics and packaging companies. Delivery companies based in the UK looking to expand overseas.

Number of Pages Required

5+ page

Font styles to use
Sans Serif

Colors
aaaaaa
dbdbdb
e6e6e6
c4c4c4
cbcbcb
c9c9c9
ec1f27
3176b5
0355a3

Requirements
Must have
• Landing Page.
• What we do.
• Who we are.
• Modules.
• Testimonies (password protected)
• Contact us.
• Interactive for mobile operating systems.
• Scrolling website.
• Short stock video showing on key pages.
• Very well polished fonts and buttons. A sharp and well executed website is required.
• Simplicity in feeling.
• To the point on message.
• Refined wording and copyrighting / messaging
• A link to our sub brand and product Brisk Parcels
• Capture interest so people read further.
Nice to have
• A polished video to explain what we do on landing page. Clipmarrow.net have some good options but not sure how professional they will look.
Should not have
• Bad graphics and colours.
• Not lots of clicks. Less as possible
• Complex message

```html
<!DOCTYPE html>
<html lang="en">
<head>
<meta charset="utf-8">
<title>Brisk. Technology</title>
<link rel="stylesheet" href="https://fonts.googleapis.com/css2?family=Montserrat:wght@400;500;600;700&display=swap">
<style>
:root{
  --red:#ec1f27;
  --blue:#3176b5;
  --navy:#0355a3;
  --ink:#1d1d1d;
  --grey:#6f6f6f;
  --light:#e6e6e6;
  --line:#c4c4c4;
  --footer:#231f20;
  --white:#ffffff;
}
*{margin:0;padding:0;box-sizing:border-box}
html,body{width:1200px;height:2362px;overflow:hidden}
body{font-family:"Montserrat",Arial,sans-serif;color:var(--ink);background:var(--white);position:relative}
.abs{position:absolute}
/* header */
.site-header{position:absolute;left:0;top:0;width:1200px;height:80px;background:var(--white)}
.brand{position:absolute;left:82px;top:24px;font-size:24px;font-weight:700;color:var(--red);letter-spacing:-.3px;white-space:nowrap}
.nav{position:absolute;top:33px;font-size:11px;font-weight:600;letter-spacing:.6px}
.nav a{position:absolute;white-space:nowrap;color:var(--ink);text-decoration:none}
.nav a.active{color:var(--blue)}
.nav a.active::after{content:"";position:absolute;left:-6px;right:-6px;top:40px;height:2px;background:var(--blue)}
.btn{position:absolute;display:flex;align-items:center;justify-content:center;font-size:10.5px;font-weight:700;letter-spacing:.8px;color:var(--white);text-transform:uppercase;white-space:nowrap}
.btn-blue{background:var(--blue)}
.btn-red{background:var(--red)}
.btn-outline{border:1.5px solid var(--red);color:var(--red);background:transparent}
/* hero */
.hero{position:absolute;left:0;top:80px;width:1200px;height:520px;background:linear-gradient(100deg,#5a5047 0%,#7b6c5c 35%,#4f4a47 65%,#6d5f52 100%)}
.hero-title{position:absolute;left:156px;top:172px;font-size:30px;line-height:39px;font-weight:700;color:var(--white);text-transform:uppercase}
.play{position:absolute;left:855px;top:170px;width:170px;height:170px;border-radius:50%;background:rgba(255,255,255,.28)}
/* intro */
.intro-title{position:absolute;left:0;top:658px;width:1200px;text-align:center;font-size:24px;line-height:30px;font-weight:500}
.intro-copy{position:absolute;left:160px;width:880px;text-align:center;font-size:12.5px;line-height:18px;color:var(--grey)}
.sub-brand{position:absolute;top:930px;font-size:24px;font-weight:700;color:var(--red);width:220px;text-align:center;white-space:nowrap}
.divider-v{position:absolute;left:600px;top:910px;width:1px;height:78px;background:var(--line)}
/* what we do */
.what-we-do{position:absolute;left:0;top:1052px;width:1200px;height:446px;background:linear-gradient(100deg,#3f3a35 0%,#5c5248 45%,#3a3632 100%)}
.eyebrow{position:absolute;left:0;width:1200px;text-align:center;font-size:11px;font-weight:700;letter-spacing:1.2px;color:var(--white)}
.section-title-light{position:absolute;left:0;width:1200px;text-align:center;font-size:23px;line-height:29px;font-weight:500;color:var(--white)}
.tab{position:absolute;font-size:14px;font-weight:700;letter-spacing:1px;color:var(--white);width:300px;text-align:center}
.copy-light{position:absolute;left:190px;width:820px;text-align:center;font-size:12.5px;line-height:19px;color:var(--white)}
/* parcels */
.parcels-title{position:absolute;left:156px;top:1563px;width:420px;font-size:19px;line-height:23px;font-weight:600}
.feature-list{position:absolute;left:156px;top:1656px;list-style:none;font-size:12px;color:var(--grey)}
.feature-list li{height:24.5px;display:flex;align-items:center;gap:8px}
.photo-courier{position:absolute;left:612px;top:1563px;width:432px;height:319px;background:linear-gradient(120deg,#cbb79a 0%,#a58f72 45%,#e2d3bd 100%)}
/* footer */
.site-footer{position:absolute;left:0;top:2025px;width:1200px;height:337px;background:var(--footer)}
.cta-panel{position:absolute;left:156px;top:1947px;width:888px;height:160px;background:var(--light);display:flex}
.cta{flex:1;position:relative;display:flex;flex-direction:column;align-items:center;padding-top:34px}
.cta+.cta::before{content:"";position:absolute;left:0;top:30px;bottom:30px;width:1px;background:var(--line)}
.cta-label{margin-top:14px;font-size:15px;font-weight:600;color:var(--navy)}
.cta-label.active{color:var(--red);text-decoration:underline}
.foot-head{position:absolute;top:2170px;font-size:11px;font-weight:600;letter-spacing:1.2px;color:var(--blue)}
.foot-text{position:absolute;top:2200px;font-size:12px;line-height:23px;color:#c9c9c9;white-space:nowrap}
.foot-text u{color:#dbdbdb}
.social{position:absolute;top:2206px;width:34px;height:34px;border-radius:50%;background:#aaaaaa}
.social.active{background:var(--red)}
.rule{position:absolute;left:133px;top:2287px;width:935px;height:1px;background:#3d393a}
.copyright{position:absolute;left:0;top:2316px;width:1200px;text-align:center;font-size:11px;color:#c9c9c9}
.copyright span{color:var(--red)}
</style>
</head>
<body>

<header class="site-header">
  <div class="brand">Brisk. Technology</div>
  <nav class="nav">
    <a class="active" style="left:368px">HOME</a>
    <a style="left:439px">WHAT WE DO</a>
    <a style="left:552px">WHO WE ARE</a>
    <a style="left:666px">MODULES</a>
    <a style="left:758px">TESTIMAONIES</a>
    <a style="left:877px">CONTACT US</a>
  </nav>
  <div class="btn btn-blue" style="left:992px;top:24px;width:128px;height:31px">Request a demo</div>
</header>

<section class="hero" role="img" aria-label="Warehouse with shelves of boxed pallets and a worker driving a forklift">
  <h1 class="hero-title">Manage your carriers,<br>your delivery speeds, and<br>your costs</h1>
  <div class="btn btn-red" style="left:156px;top:310px;width:143px;height:31px">Discover products</div>
  <div class="play">
    <svg class="abs" style="left:68px;top:60px" width="40" height="50" viewBox="0 0 40 50"><path d="M0 0 L40 25 L0 50 Z" fill="#fff"/></svg>
  </div>
</section>

<section>
  <h2 class="intro-title">Brisk. Technology &amp; Parcel Solutions Built To Help Develop<br>&amp; Manage Your Global Delivery Network</h2>
  <p class="intro-copy" style="top:746px">Working closely with Ecommerce, Brisk. Technology have developed solutions purely focused on delivering what's required within the global delivery marketplace. Meeting all needs and more for Retailers and Global Delivery Solution providers</p>
  <p class="intro-copy" style="top:797px">Allowing customers to grow at a fast pace; most importantly providing tools to help them manage their global delivery network supported by "Dynamic Real Time Visibility" management tools.</p>
  <div class="btn btn-blue" style="left:384px;top:856px;width:203px;height:31px">Brisk. Parcel</div>
  <div class="btn btn-red" style="left:612px;top:856px;width:203px;height:31px">Brisk. Technology</div>
  <div class="sub-brand" style="left:370px">Brisk Parcels</div>
  <div class="divider-v"></div>
  <div class="sub-brand" style="left:610px">Brisk. Technology</div>
</section>

<section class="what-we-do" role="img" aria-label="Dim warehouse aisle with a forklift among tall pallet racks">
  <div class="eyebrow" style="top:76px">WHAT WE DO</div>
  <h2 class="section-title-light" style="top:100px">Solution Developed To Help you Build &amp; Manage Your<br>Global Delivery&nbsp; Network</h2>
  <div class="tab" style="left:222px;top:190px">LOGISTIC PROVIDERS</div>
  <div class="tab" style="left:678px;top:190px">RETAILERS DELIVERY</div>
  <div class="abs" style="left:160px;top:224px;width:880px;height:1px;background:rgba(255,255,255,.45)"></div>
  <div class="abs" style="left:160px;top:223px;width:430px;height:3px;background:var(--red)"></div>
  <p class="copy-light" style="top:254px">Brisk. Technology gives logistic companies to enhance their platform to implement and manage their extended delivery partners.&nbsp; Full end to end solution covers all the key elements, allowing Carriers to implement services manage all delivery activities via 1 single platform ...</p>
  <div class="btn btn-red" style="left:528px;top:335px;width:127px;height:31px">Read more</div>
</section>

<section>
  <h2 class="parcels-title">Brisk. Parcels Delivering To Complex Lanes Providing A Fully Managed Secure Delivery Experience</h2>
  <ul class="feature-list">
    <li><svg width="12" height="10" viewBox="0 0 12 10"><path d="M1 5 L4.5 8.5 L11 1" fill="none" stroke="#3176b5" stroke-width="2"/></svg>Fully Managed End To End Delivery Solution</li>
    <li><svg width="12" height="10" viewBox="0 0 12 10"><path d="M1 5 L4.5 8.5 L11 1" fill="none" stroke="#3176b5" stroke-width="2"/></svg>Delivery Solution Suited For Local Consumers</li>
    <li><svg width="12" height="10" viewBox="0 0 12 10"><path d="M1 5 L4.5 8.5 L11 1" fill="none" stroke="#3176b5" stroke-width="2"/></svg>Last Mile Printed At Pack Bench</li>
    <li><svg width="12" height="10" viewBox="0 0 12 10"><path d="M1 5 L4.5 8.5 L11 1" fill="none" stroke="#3176b5" stroke-width="2"/></svg>Supported By End To End Tracking</li>
    <li><svg width="12" height="10" viewBox="0 0 12 10"><path d="M1 5 L4.5 8.5 L11 1" fill="none" stroke="#3176b5" stroke-width="2"/></svg>Secure Customs Set Up</li>
    <li><svg width="12" height="10" viewBox="0 0 12 10"><path d="M1 5 L4.5 8.5 L11 1" fill="none" stroke="#3176b5" stroke-width="2"/></svg>Service Supported By Account Management Tools</li>
    <li><svg width="12" height="10" viewBox="0 0 12 10"><path d="M1 5 L4.5 8.5 L11 1" fill="none" stroke="#3176b5" stroke-width="2"/></svg>Service Managed Bt Brisk Parcels Service Support Team</li>
  </ul>
  <div class="btn btn-outline" style="left:156px;top:1848px;width:144px;height:31px">Let's talk</div>
  <div class="photo-courier" role="img" aria-label="Courier handing a parcel to a customer signing a clipboard"></div>
</section>

<footer class="site-footer"></footer>

<div class="cta-panel">
  <div class="cta">
    <svg width="44" height="44" viewBox="0 0 44 44" fill="none" stroke="#1d1d1d" stroke-width="2"><path d="M8 10 L14 6 L20 14 L16 18 Q20 26 26 30 L30 26 L38 32 L34 38 Q20 40 8 24 Z"/><rect x="26" y="4" width="14" height="12" stroke="#ec1f27"/></svg>
    <div class="cta-label">Need Help? Contact Us</div>
  </div>
  <div class="cta">
    <svg width="44" height="44" viewBox="0 0 44 44" fill="none" stroke="#1d1d1d" stroke-width="2"><path d="M18 40 L12 28 Q11 24 15 25 L18 28 L18 12 Q20 9 22 12 L22 22 L32 24 Q35 25 34 30 L32 40"/><path d="M14 12 A6 6 0 0 1 26 12" stroke="#ec1f27"/><path d="M10 12 A10 10 0 0 1 30 12" stroke="#ec1f27"/></svg>
    <div class="cta-label active">Request a Demo</div>
  </div>
  <div class="cta">
    <svg width="44" height="44" viewBox="0 0 44 44" fill="none" stroke="#1d1d1d" stroke-width="2"><circle cx="22" cy="16" r="8"/><path d="M10 16 A12 12 0 0 1 34 16" stroke="#ec1f27"/><path d="M8 40 Q8 28 22 28 Q36 28 36 40 Z"/><rect x="16" y="34" width="12" height="6" stroke="#ec1f27"/></svg>
    <div class="cta-label">Request a Quote</div>
  </div>
</div>

<div class="foot-head" style="left:156px">ADDRESS:</div>
<div class="foot-text" style="left:156px">4410 Larkfield Avenue,<br>Denbrook, KT 60214</div>
<div class="foot-head" style="left:460px">CONTACT US:</div>
<div class="foot-text" style="left:460px">Phone: 014 - 552 - 7310<br>Email:&nbsp; <u>info@brisktechnology.com</u></div>
<div class="foot-head" style="left:764px">FOLLOW US:</div>
<div class="social" style="left:765px"></div>
<div class="social active" style="left:805px"></div>
<div class="social" style="left:847px"></div>
<div class="social" style="left:889px"></div>
<svg class="abs" style="left:1110px;top:2172px" width="18" height="20" viewBox="0 0 18 20"><path d="M9 0 L18 20 L9 15 L0 20 Z" fill="#3176b5"/></svg>
<div class="rule"></div>
<div class="copyright">© 2018 <span>Brisk Technology.</span> All Rights Reserved.&nbsp;&nbsp;&nbsp;&nbsp;Terms &amp; Conditions&nbsp;&nbsp;&nbsp;|&nbsp;&nbsp;&nbsp;Privacy Policy</div>

</body>
</html>
```